AWESOME CYBER MONDAY SALE AD NEEDED

Create a Cyber Monday ad for nitrile gloves. We are offering a box of 100, no-powder, exam grade nitrile gloves, for $9.99. No limit. Each case is $99. Create something simple, eye catching, cool. KelpTorch.com. Sale ends on December 4th. While supplies last. We are a local medical supply company in Hawaii that serves the general public in addition to local businesses, government, etc. Gloves are in short supply and we have tons of inventory ready to sell.

Target Market(s)

Businesses that use supplies such as gloves

Industry/Entity Type

medical supplies

Requirements
Must have
• The company logo, website, picture of gloves and pricing.

```html
<!DOCTYPE html>
<html lang="en">
<head>
<meta charset="utf-8">
<title>KelpTorch.com — Cyber Monday Nitrile Glove Sale</title>
<link href="https://fonts.googleapis.com/css2?family=Montserrat:wght@700;800;900&display=swap" rel="stylesheet">
<style>
  :root {
    --blue: #0796df;
    --green: #3bb44a;
    --white: #ffffff;
    --grey: #6d6e70;
    --glove-light: #c9e4f5;
    --glove-mid: #8fc4e6;
  }
  * { margin: 0; padding: 0; box-sizing: border-box; }
  html, body { width: 1200px; height: 1200px; overflow: hidden; background: var(--white); }
  body { font-family: "Montserrat", sans-serif; font-weight: 800; }

  .ad { position: relative; width: 1200px; height: 1200px; overflow: hidden; background: var(--white); }

  .stripe-band {
    position: absolute; left: 0; top: 0; width: 1200px; height: 65px;
    background: repeating-linear-gradient(90deg,
      var(--blue) 0 46px, var(--green) 46px 57px, var(--white) 57px 77px);
  }

  .headline-banner { position: absolute; left: 0; top: 140px; width: 1200px; height: 240px; }

  .tag {
    position: absolute; background: var(--green); color: var(--white);
    border-radius: 8px; text-transform: uppercase; letter-spacing: 1px;
    display: flex; align-items: center; justify-content: center;
    transform-origin: center;
  }
  .tag--miss { left: 86px; top: 90px; width: 506px; height: 86px; font-size: 52px; transform: rotate(-4deg); }
  .tag--special { left: 268px; top: 343px; width: 240px; height: 68px; font-size: 44px; transform: rotate(-4deg); }

  .limited-badge {
    position: absolute; left: 984px; top: 301px; width: 206px; height: 206px;
    border-radius: 50%; background: var(--blue); color: var(--white);
    display: flex; align-items: center; justify-content: center; text-align: center;
    font-size: 25px; line-height: 1.2; letter-spacing: 1px;
  }
  .limited-badge span { display: block; transform: rotate(8deg); }

  .glove-photo {
    position: absolute; left: 652px; top: 440px; width: 548px; height: 760px;
    border-radius: 220px 160px 0 0;
    background: radial-gradient(ellipse at 45% 45%, var(--glove-light) 0%, var(--glove-mid) 60%, rgba(143,196,230,0) 100%);
  }

  .features { position: absolute; left: 49px; top: 558px; list-style: none; color: var(--green); font-size: 50px; line-height: 53px; letter-spacing: 1px; }
  .features li::after { content: ""; }
  .tick { display: inline-block; width: 30px; height: 30px; margin-left: 10px; vertical-align: -3px; }

  .product-title { position: absolute; left: 46px; top: 732px; color: var(--blue); font-size: 82px; line-height: 76px; letter-spacing: 1px; }

  .price-row { position: absolute; display: flex; align-items: center; gap: 20px; }
  .price-row--box { left: 300px; top: 876px; }
  .price-row--case { left: 300px; top: 1002px; }
  .price-label { width: 196px; text-align: right; font-size: 30px; line-height: 29px; letter-spacing: 1px; }
  .price-label .unit { color: var(--blue); display: block; }
  .price-label .for { color: var(--green); display: block; }
  .price-pill { background: var(--green); color: var(--white); display: flex; align-items: baseline; justify-content: center; }
  .price-pill--box { width: 208px; height: 93px; border-radius: 44px; font-size: 82px; padding-top: 2px; }
  .price-pill--box .cur { font-size: 52px; }
  .price-pill--box .cents { font-size: 46px; }
  .price-pill--case { width: 112px; height: 70px; border-radius: 26px; font-size: 48px; margin-left: -6px; margin-top: 6px; padding-top: 4px; }
  .price-pill--case .cur { font-size: 28px; }

  .brand { position: absolute; left: 52px; top: 1118px; display: flex; align-items: center; gap: 10px; color: var(--green); font-size: 30px; font-weight: 800; }
  .brand-dot { width: 18px; height: 18px; border-radius: 50%; background: var(--green); }

  .sale-ends {
    position: absolute; left: 310px; top: 1112px; width: 626px; height: 88px;
    background: var(--green); color: var(--white); border-radius: 60px 60px 0 0;
    display: flex; align-items: center; justify-content: center;
    font-size: 29px; letter-spacing: 1px; padding-bottom: 10px;
  }
</style>
</head>
<body>
<main class="ad">
  <div class="stripe-band"></div>

  <svg class="headline-banner" viewBox="0 140 1200 240" width="1200" height="240" aria-label="Cyber Monday">
    <defs>
      <clipPath id="banner-clip">
        <path d="M22 359 C 40 260, 150 190, 260 175 L 578 154 L 1196 154 L 1196 230 C 1170 290, 1120 320, 1060 359 Z"/>
      </clipPath>
    </defs>
    <path d="M22 359 C 40 260, 150 190, 260 175 L 578 154 L 1196 154 L 1196 230 C 1170 290, 1120 320, 1060 359 Z" fill="var(--blue)"/>
    <g clip-path="url(#banner-clip)" font-family="Montserrat, sans-serif" font-weight="800" font-size="122">
      <text x="86" y="197" textLength="1076" lengthAdjust="spacingAndGlyphs" fill="none" stroke="var(--white)" stroke-width="4">CYBER MONDAY</text>
      <text x="86" y="293" textLength="1076" lengthAdjust="spacingAndGlyphs" fill="var(--white)">CYBER MONDAY</text>
      <text x="86" y="389" textLength="1076" lengthAdjust="spacingAndGlyphs" fill="none" stroke="var(--white)" stroke-width="4">CYBER MONDAY</text>
    </g>
  </svg>

  <div class="tag tag--miss">Don’t miss this</div>
  <div class="tag tag--special">Special</div>

  <div class="glove-photo" role="img" aria-label="Photo of a pair of light blue nitrile exam gloves being pulled on"></div>

  <div class="limited-badge"><span>ONLY FOR<br>A LIMITED<br>TIME</span></div>

  <ul class="features">
    <li>PREMIUM<svg class="tick" viewBox="0 0 30 30"><path d="M4 16 L12 25 L27 3" fill="none" stroke="var(--blue)" stroke-width="4" stroke-linecap="round"/></svg></li>
    <li>NON-STERILE<svg class="tick" viewBox="0 0 30 30"><path d="M4 16 L12 25 L27 3" fill="none" stroke="var(--blue)" stroke-width="4" stroke-linecap="round"/></svg></li>
    <li>POWDER-FREE<svg class="tick" viewBox="0 0 30 30"><path d="M4 16 L12 25 L27 3" fill="none" stroke="var(--blue)" stroke-width="4" stroke-linecap="round"/></svg></li>
  </ul>

  <h1 class="product-title">NITRILE EXAM<br>GLOVES</h1>

  <div class="price-row price-row--box">
    <p class="price-label"><span class="unit">BOXES</span><span class="for">FOR ONLY</span></p>
    <p class="price-pill price-pill--box"><span class="cur">$</span>9<span class="cents">.99</span></p>
  </div>

  <div class="price-row price-row--case">
    <p class="price-label"><span class="unit">CASES</span><span class="for">FOR ONLY</span></p>
    <p class="price-pill price-pill--case"><span class="cur">$</span>99</p>
  </div>

  <div class="brand"><span class="brand-dot"></span>KelpTorch.com</div>

  <div class="sale-ends">SALE ENDS DECEMBER 4TH, 2021</div>
</main>
</body>
</html>
```